Silver Kettle Studio Marketing Postcard

I need a 2 sided A6 postcard to distribute to potential clients. The postcard will include the business logo and information about the service we provide and contact information. I want it to be stylish and to compliment the business card. I've attached the business card and logo files as well as some text to use. I have other source files (.eps and.ai) if required please message me. I don't need the postal address or my position included on the postcard.
I am open to portrait or landscape designs, whatever you think is most stylish and eye catching.

```html
<!DOCTYPE html>
<html lang="en">
<head>
<meta charset="utf-8">
<title>Silver Kettle Studio Postcard</title>
<link rel="stylesheet" href="https://fonts.googleapis.com/css2?family=PT+Sans:wght@400;700&family=Ubuntu:wght@400;500;700&display=swap">
<style>
  :root {
    --page: #e9e7e3;
    --green: #6aac2b;
    --green-deep: #1f7a2a;
    --green-light: #4fae3a;
    --navy: #1c2838;
    --red: #d8261c;
    --yellow: #f2c318;
    --white: #ffffff;
    --ink: #2a2a2a;
    --photo-grey: #d9d9d9;
    --dark-green-text: #1d3a16;
  }
  * { box-sizing: border-box; margin: 0; padding: 0; }
  html, body { width: 1200px; height: 927px; overflow: hidden; }
  body {
    background: var(--page);
    font-family: "PT Sans", Arial, sans-serif;
    position: relative;
  }
  .card {
    position: absolute;
    width: 636px;
    height: 452px;
    overflow: hidden;
    box-shadow: 0 4px 14px rgba(0,0,0,.25);
  }
  /* ---------- Front ---------- */
  .card--front { left: 24px; top: 27px; background: var(--white); }
  .front__topbar { position: absolute; left: 0; top: 0; width: 100%; height: 19px; background: #cfcfcf; }
  .front__banner {
    position: absolute; left: 0; top: 19px; width: 380px; height: 140px;
    background: linear-gradient(180deg, var(--green-light), var(--green-deep));
    clip-path: polygon(0 0, 84% 0, 94% 50%, 100% 82%, 0 82%);
  }
  .front__headline {
    position: absolute; left: 0; top: 30px; width: 330px; text-align: center;
    font-family: "Ubuntu", Arial, sans-serif; font-weight: 700; line-height: 1.05;
  }
  .front__headline .lead { display: block; color: var(--white); font-size: 35px; }
  .front__headline .shout {
    display: block; color: var(--red); font-size: 38px;
    text-shadow: -2px -2px 0 #fff, 2px -2px 0 #fff, -2px 2px 0 #fff, 2px 2px 0 #fff;
  }
  .front__question {
    position: absolute; left: 380px; top: 42px; width: 240px;
    font-size: 17px; line-height: 1.25; color: var(--ink);
  }
  .front__photo {
    position: absolute; left: 0; top: 134px; width: 337px; height: 318px;
    background: radial-gradient(circle at 50% 45%, #efefef, var(--photo-grey));
  }
  .front__panel {
    position: absolute; left: 337px; top: 134px; width: 299px; height: 318px;
    background: var(--green); color: var(--white);
  }
  .front__help {
    position: absolute; left: 10px; top: 14px;
    font-family: "Ubuntu", Arial, sans-serif; font-weight: 500; font-size: 19px;
  }
  .brand-name {
    font-family: "PT Sans", Arial, sans-serif; font-weight: 400; color: var(--white);
  }
  .front__brand {
    position: absolute; left: 0; top: 95px; width: 100%; text-align: center;
    font-size: 34px; line-height: 1.1;
  }
  .contact { position: absolute; color: var(--white); }
  .contact__note { font-size: 15px; }
  .phone-box {
    position: relative; margin-top: 5px; width: 194px; height: 42px;
    border: 2px solid var(--white); border-left: none; padding-left: 22px;
  }
  .phone-box__icon { position: absolute; left: -4px; top: 4px; width: 18px; height: 32px; }
  .phone-box__label {
    position: absolute; left: 18px; top: -9px; padding: 0 4px; background: inherit;
    font-size: 8.5px; font-weight: 700; letter-spacing: .3px;
  }
  .phone-box__number {
    display: block; padding-top: 9px; font-family: "Ubuntu", Arial, sans-serif;
    font-weight: 700; font-size: 22px; color: var(--white);
  }
  .contact__lines { margin-top: 8px; font-size: 12.5px; line-height: 1.3; text-align: center; }
  .front__panel .contact { left: 14px; top: 208px; }
  .front__panel .phone-box__label { background: var(--green); }
  /* ---------- Back ---------- */
  .card--back { left: 528px; top: 442px; background: var(--green); }
  .back__split { position: absolute; left: 0; top: 0; width: 380px; height: 452px; }
  .back__brand {
    position: absolute; left: 24px; top: 32px; font-size: 50px; line-height: 1.02;
  }
  .back__intro {
    position: absolute; left: 27px; top: 208px; width: 290px;
    color: var(--yellow); font-size: 15px; line-height: 1.25;
  }
  .back__intro p + p { margin-top: 14px; }
  .services { position: absolute; left: 40px; top: 328px; list-style: none; color: var(--white); font-size: 15px; line-height: 1.18; }
  .services li { display: flex; align-items: center; gap: 6px; }
  .services svg { width: 13px; height: 13px; }
  .back__pitch {
    position: absolute; left: 380px; top: 176px; width: 250px; text-align: center;
    font-family: "Ubuntu", Arial, sans-serif; font-weight: 700;
  }
  .back__pitch .ask { display: block; color: var(--dark-green-text); font-size: 26px; font-weight: 500; }
  .back__pitch .claim { display: block; color: var(--white); font-size: 31px; line-height: 1.1; margin-top: 8px; text-shadow: 1px 1px 2px rgba(0,0,0,.3); }
  .back__pitch .accent { color: var(--yellow); }
  .card--back .contact { left: 420px; top: 336px; }
  .card--back .phone-box__label { background: var(--green); }
  .card--back .contact__lines { text-align: right; }
</style>
</head>
<body>

<section class="card card--front">
  <div class="front__topbar"></div>
  <div class="front__banner"></div>
  <h1 class="front__headline">
    <span class="lead">Do you feel</span>
    <span class="shout">FRUSTRATED</span>
  </h1>
  <p class="front__question">by computers, TVs, phones, tablets and countless other digital devices?</p>
  <div class="front__photo" role="img" aria-label="Photo of a frustrated person surrounded by a tablet, laptop, desktop computer, phone and TV"></div>
  <div class="front__panel">
    <p class="front__help">WE ARE HERE TO HELP YOU!</p>
    <p class="front__brand brand-name">Silver Kettle Studio</p>
    <div class="contact">
      <p class="contact__note">Phone Conversation are free</p>
      <div class="phone-box">
        <svg class="phone-box__icon" viewBox="0 0 18 32"><path d="M14 2 C6 2 3 9 3 16 C3 23 6 30 14 30" fill="none" stroke="#fff" stroke-width="4" stroke-linecap="round"/></svg>
        <span class="phone-box__label">FREE CALL REECE</span>
        <span class="phone-box__number">0400 555 019</span>
      </div>
      <p class="contact__lines">reece@silverkettlestudio.com.au<br>www.silverkettlestudio.com.au</p>
    </div>
  </div>
</section>

<section class="card card--back">
  <svg class="back__split" viewBox="0 0 380 452" preserveAspectRatio="none">
    <path d="M0 0 H300 C345 120 330 300 352 452 H0 Z" fill="var(--navy)"/>
  </svg>
  <h2 class="back__brand brand-name">Silver Kettle<br>Studio</h2>
  <div class="back__intro">
    <p>From a simple computer health check to the purchase and installation of home networks and digital services.</p>
    <p>We also give useful product advice and maintenance tips.</p>
  </div>
  <ul class="services">
    <li><svg viewBox="0 0 13 13"><path d="M1 7 L5 11 L12 1" fill="none" stroke="#8cc63f" stroke-width="2.2"/></svg>On site support</li>
    <li><svg viewBox="0 0 13 13"><path d="M1 7 L5 11 L12 1" fill="none" stroke="#8cc63f" stroke-width="2.2"/></svg>Advice</li>
    <li><svg viewBox="0 0 13 13"><path d="M1 7 L5 11 L12 1" fill="none" stroke="#8cc63f" stroke-width="2.2"/></svg>Installation</li>
    <li><svg viewBox="0 0 13 13"><path d="M1 7 L5 11 L12 1" fill="none" stroke="#8cc63f" stroke-width="2.2"/></svg>Education</li>
  </ul>
  <div class="back__pitch">
    <span class="ask">Let us help you</span>
    <span class="claim"><span class="accent">TAME</span> YOUR<br>DIGITAL WORLD</span>
  </div>
  <div class="contact">
    <p class="contact__note">Phone Conversation are free</p>
    <div class="phone-box">
      <svg class="phone-box__icon" viewBox="0 0 18 32"><path d="M14 2 C6 2 3 9 3 16 C3 23 6 30 14 30" fill="none" stroke="#fff" stroke-width="4" stroke-linecap="round"/></svg>
      <span class="phone-box__label">FREE CALL REECE</span>
      <span class="phone-box__number">0400 555 019</span>
    </div>
    <p class="contact__lines">reece@silverkettlestudio.com.au<br>www.silverkettlestudio.com.au</p>
  </div>
</section>

</body>
</html>
```